Design & Build a WordPress Website for “Quietfern Meditation” (Australian Charity Rebrand)

We are a registered Australian charity currently known as Tavolin Meditation Australia.

We are rebranding our public identity to “Quietfern Meditation” to make the meditation practice easier to understand and more relatable for people in Australia and New Zealand.

We are looking for an experienced WordPress designer + developer to design and build a complete website that reflects:

Peace

Trust

Authentic Himalayan roots

Simplicity

Spiritual depth without being religious

Warmth, friendliness, and community feeling

This is not a corporate website. This is a meditation movement website for a non-profit organisation.

Target Market(s)

Australia and New Zealand - Age 25-65

Industry/Entity Type

Not of profit meditation organisation

Requirements
Must have
• Included in the design brief attached
Nice to have
Should not have

```html
<!DOCTYPE html>
<html lang="en">
<head>
<meta charset="utf-8">
<title>Quietfern Meditation</title>
<link href="https://fonts.googleapis.com/css2?family=Lato:wght@400;700;900&family=Inter:wght@400;500;600;700&display=swap" rel="stylesheet">
<style>
:root{
  --navy:#2e4d5f;
  --green:#71ac66;
  --green-soft:#e3efdf;
  --card:#f2f3f2;
  --text:#3a3a3a;
  --white:#ffffff;
}
*{box-sizing:border-box;margin:0;padding:0}
html,body{width:1200px;height:3989px;overflow:hidden}
body{position:relative;background:var(--white);font-family:'Inter',sans-serif;color:var(--text)}
.abs{position:absolute}
.heading{font-family:'Lato',sans-serif;color:var(--navy);font-weight:700;text-align:center}
.underline{position:absolute;height:3px;width:84px;background:var(--green);left:558px}
.btn{position:absolute;display:flex;align-items:center;justify-content:center;border-radius:30px;font-weight:700;font-size:14px;text-transform:uppercase;color:var(--white);background:var(--green)}
.btn.soft{background:var(--green-soft);color:var(--green)}
.btn.navy{background:var(--navy)}
/* header */
.logo{left:109px;top:27px;font-family:'Lato',sans-serif;font-weight:700;font-size:31px;line-height:38px;color:var(--navy)}
.logo span{display:block;color:var(--green)}
.social{display:flex;gap:9px}
.social i{width:32px;height:32px;border:1.5px solid var(--green);border-radius:50%;display:block;position:relative}
.social i::after{content:"";position:absolute;left:11px;top:11px;width:7px;height:7px;border-radius:50%;background:var(--green)}
.social i.on{background:var(--green)}
.social i.on::after{background:var(--white)}
.nav{left:439px;top:78px;display:flex;gap:0;font-size:13px;font-weight:600;color:var(--navy);line-height:22px}
.nav a{text-decoration:none;color:inherit;display:block}
/* hero */
.hero{left:0;top:130px;width:1200px;height:652px;background:linear-gradient(100deg,#8c8a6a 0%,#b3a27a 35%,#c9b58b 55%,#9a9362 80%,#6d7448 100%)}
.hero-title{left:111px;top:248px;font-family:'Lato',sans-serif;color:var(--white);font-size:40px;line-height:48px;font-weight:400}
.hero-title b{font-weight:900}
.hero-sub{left:111px;top:352px;width:480px;color:var(--white);font-size:20px;line-height:29px}
.dots{left:1135px;top:355px;display:flex;flex-direction:column;gap:10px}
.dots i{width:15px;height:15px;border:2px solid var(--white);border-radius:50%;display:block}
.dots i.on{background:var(--white)}
/* sessions */
.card{position:absolute;top:964px;width:317px;height:470px;background:var(--card);border-radius:18px;overflow:hidden;text-align:center}
.card.active{background:var(--white);height:496px;box-shadow:0 6px 18px rgba(0,0,0,.16)}
.card .ph{height:240px}
.card h3{font-size:17px;font-weight:700;color:var(--navy);margin:24px 20px 8px;line-height:26px;text-transform:uppercase}
.card p{font-size:15px;line-height:24px;color:#444;margin:0 14px}
.card .btn{position:relative;margin:14px auto 0;width:155px;height:44px}
.arrow{width:33px;height:33px;border-radius:50%}
/* about */
.about{left:0;top:1565px;width:1200px;height:647px;background:linear-gradient(180deg,#9aa7b4 0%,#dfe4e8 45%,#b6bec4 100%)}
.about-card{left:629px;top:1662px;width:459px;height:462px;background:var(--white);border-radius:14px;text-align:center}
.about-card h2{font-family:'Lato',sans-serif;color:var(--navy);font-size:39px;line-height:47px;font-weight:700;margin-top:48px}
.about-card p{font-size:16px;line-height:25px;margin:22px 34px 0;color:#333}
/* how */
.how{left:0;top:2212px;width:1200px;height:566px;background:var(--green)}
.step{position:absolute;top:2160px;width:210px;text-align:center}
.ico{position:absolute;width:96px;height:96px;border-radius:50%;background:var(--white);top:2370px}
.ico::before{content:"";position:absolute;inset:5px;border:2px dashed var(--navy);border-radius:50%}
.step-t{position:absolute;top:2486px;width:220px;text-align:center;color:var(--white);font-weight:700;font-size:17px;line-height:26px}
.step-p{position:absolute;top:2542px;width:220px;text-align:center;color:#eef5ec;font-size:15px;line-height:24px}
/* articles */
.date{display:inline-flex;align-items:center;gap:5px;background:var(--green);color:var(--white);font-size:11px;font-weight:700;border-radius:16px;height:32px;padding:0 14px}
.art-t{color:var(--navy);font-weight:700;font-size:17px;line-height:26px;text-transform:uppercase}
.more{color:var(--green);font-weight:700;font-size:14px;text-decoration:underline}
/* footer */
.footer{left:0;top:3560px;width:1200px;height:429px;background:var(--navy)}
.f-h{color:var(--white);font-weight:600;font-size:18px}
.links{list-style:none;color:var(--white);font-size:14px;line-height:32px}
.links li::before{content:"";display:inline-block;width:5px;height:5px;border-radius:50%;background:var(--green);margin-right:19px;vertical-align:middle}
.ci{position:absolute;width:36px;height:36px;border-radius:50%;background:var(--white);display:flex;align-items:center;justify-content:center}
.cl{color:var(--white);font-size:14px;font-weight:600;line-height:20px}
.cl small{display:block;font-size:11px;font-weight:400;line-height:16px}
</style>
</head>
<body>

<!-- Header -->
<div class="abs logo">QUIETFERN<span>MEDITATION</span></div>
<div class="abs social" style="left:557px;top:21px"><i></i><i class="on"></i><i></i><i></i></div>
<div class="btn soft" style="left:722px;top:17px;width:152px;height:40px">Donate Now</div>
<div class="btn" style="left:885px;top:17px;width:203px;height:40px">Join a Free Session</div>
<nav class="abs nav">
  <a style="width:75px;color:var(--green);text-decoration:underline">HOME</a>
  <a style="width:137px">ABOUT THE<br>ORGANISATION</a>
  <a style="width:117px">MEDITATION<br>SESSIONS</a>
  <a style="width:112px">EVENTS &amp;<br>PROGRAMS</a>
  <a style="width:117px">RESOURCES</a>
  <a>CONTACT US</a>
</nav>

<!-- Hero -->
<div class="abs hero" role="img" aria-label="Photo of a woman with eyes closed and hands on her chest, breathing calmly outdoors in warm sunlight"></div>
<h1 class="abs hero-title">ANCIENT WISDOM.<br><b>MODERN LIFE.</b></h1>
<p class="abs hero-sub">A simple, effortless meditation practice taught freely to help you experience calm, clarity, and balance in everyday life.</p>
<div class="btn" style="left:111px;top:462px;width:205px;height:41px">Join a Free Session</div>
<div class="abs dots"><i></i><i class="on"></i><i></i><i></i></div>
<svg class="abs" style="left:0;top:600px" width="1200" height="190" viewBox="0 0 1200 190">
  <path d="M0,150 C220,40 420,90 640,150 C860,205 1040,170 1200,10 L1200,190 L0,190 Z" fill="#fff"/>
  <path d="M0,145 C200,40 400,75 620,130 C850,185 1040,150 1200,12 L1200,50 C1060,180 860,215 640,160 C420,105 230,60 0,150 Z" fill="var(--green)"/>
</svg>

<!-- Sessions -->
<h2 class="abs heading" style="left:0;top:856px;width:1200px;font-size:48px;font-weight:700">MEDITATION SESSIONS</h2>
<div class="underline" style="top:915px"></div>
<svg class="abs arrow" style="left:36px;top:1196px" viewBox="0 0 33 33"><circle cx="16.5" cy="16.5" r="16.5" fill="#bdbdbd"/><path d="M19,9 L12,16.5 L19,24" stroke="#fff" stroke-width="4" fill="none"/></svg>
<svg class="abs arrow" style="left:1131px;top:1196px" viewBox="0 0 33 33"><circle cx="16.5" cy="16.5" r="16.5" fill="var(--green)"/><path d="M14,9 L21,16.5 L14,24" stroke="#fff" stroke-width="4" fill="none"/></svg>

<div class="card" style="left:103px">
  <div class="ph" role="img" aria-label="Photo of a hiker sitting on a hill looking at a sunset over misty valleys" style="background:linear-gradient(180deg,#e9a55a,#b47a4b 60%,#4a4c3c)"></div>
  <h3>Self Realisation</h3>
  <p>Lorem ipsum dolor sit amet, consectetur adipiscing elit, sed do eiusmod tempor incididunt ut labore et dolore magna aliqua ad minimea.</p>
  <div class="btn soft">Learn More</div>
</div>
<div class="card active" style="left:437px">
  <div class="ph" role="img" aria-label="Photo of a person meditating on a rock above a sea of clouds at sunrise" style="background:linear-gradient(180deg,#b9a6a0,#d9b69a 45%,#5f5e5b)"></div>
  <h3>Improved Physical<br>Health</h3>
  <p>Lorem ipsum dolor sit amet, consectetur adipiscing elit, sed do eiusmod tempor incididunt ut labore et dolore magna aliqua ad minimea.</p>
  <div class="btn">Learn More</div>
</div>
<div class="card" style="left:771px">
  <div class="ph" role="img" aria-label="Photo of a smiling woman relaxing on a sofa with hands behind her head" style="background:linear-gradient(180deg,#e6e7e3,#d9c08a 60%,#c9a148)"></div>
  <h3>Peace of Mind</h3>
  <p>Lorem ipsum dolor sit amet, consectetur adipiscing elit, sed do eiusmod tempor incididunt ut labore et dolore magna aliqua ad minimea.</p>
  <div class="btn soft">Learn More</div>
</div>

<!-- About -->
<div class="abs about" role="img" aria-label="Background photo of snowy mountain peaks rising above clouds"></div>
<div class="abs" style="left:110px;top:1648px;width:488px;height:488px;border-radius:50%;background:var(--white)"></div>
<div class="abs" role="img" aria-label="Photo of a person meditating on a wooden jetty facing misty forested hills" style="left:155px;top:1675px;width:436px;height:436px;border-radius:50%;background:linear-gradient(180deg,#c9c2a2,#a9a47a 40%,#6f6748 70%,#8e7c63)"></div>
<div class="abs about-card">
  <h2>WHAT IS QUIETFERN<br>MEDITATION?</h2>
  <div style="width:84px;height:3px;background:var(--green);margin:4px auto 0"></div>
  <p>Quietfern Meditation is a simple, natural technique that allows the mind and body to settle into deep rest. Unlike methods that require concentration or control, this practice is effortless. You don't try to stop thoughts. You simply allow the mind to relax — and stillness happens naturally.</p>
  <div class="btn" style="position:relative;margin:22px auto 0;width:155px;height:44px">Learn More</div>
</div>

<!-- How it works -->
<div class="abs how"></div>
<h2 class="abs heading" style="left:0;top:2270px;width:1200px;font-size:48px;color:var(--white)">HOW IT WORKS</h2>
<div class="underline" style="top:2328px;background:var(--white)"></div>

<div class="ico" style="left:176px"><svg class="abs" style="left:28px;top:26px" width="40" height="44" viewBox="0 0 40 44" fill="var(--navy)"><rect x="14" y="0" width="16" height="11" rx="2"/><circle cx="10" cy="20" r="5"/><circle cx="29" cy="20" r="5"/><path d="M1,40 a9,9 0 0 1 18,0 Z M20,40 a9,9 0 0 1 18,0 Z"/></svg></div>
<div class="ico" style="left:427px"><svg class="abs" style="left:28px;top:24px" width="40" height="48" viewBox="0 0 40 48" fill="var(--navy)"><circle cx="22" cy="12" r="8"/><rect x="19" y="21" width="6" height="5"/><path d="M2,46 L2,32 L20,32 L30,38 L28,42 L12,40 L10,46 Z"/></svg></div>
<div class="ico" style="left:678px"><svg class="abs" style="left:26px;top:24px" width="44" height="48" viewBox="0 0 44 48" fill="var(--navy)"><circle cx="24" cy="13" r="11"/><circle cx="24" cy="13" r="4" fill="#fff"/><path d="M2,46 L2,32 L20,32 L30,36 L40,30 L42,34 L28,44 L12,42 L10,46 Z"/></svg></div>
<div class="ico" style="left:929px"><svg class="abs" style="left:24px;top:26px" width="48" height="44" viewBox="0 0 48 44" fill="var(--navy)"><circle cx="10" cy="8" r="5"/><circle cx="24" cy="6" r="5"/><circle cx="38" cy="8" r="5"/><path d="M2,26 a8,8 0 0 1 16,0 Z M16,24 a8,8 0 0 1 16,0 Z M30,26 a8,8 0 0 1 16,0 Z"/><path d="M6,34 L18,28 L30,28 L42,34 L34,42 L14,42 Z"/></svg></div>

<div class="step-t" style="left:114px">JOIN A FREE INTRO<br>SESSION</div>
<div class="step-t" style="left:365px">LEARN<br>THE TECHNIQUE</div>
<div class="step-t" style="left:616px">PRACTICE DAILY</div>
<div class="step-t" style="left:867px">GROW WITH THE<br>COMMUNITY</div>
<p class="step-p" style="left:114px">Lorem ipsum dolor sit amet, consectetur adipiscing elit, sed do eiusmod tempor incidi laborea.</p>
<p class="step-p" style="left:365px">Lorem ipsum dolor sit amet, consectetur adipiscing elit, sed do eiusmod tempor incidi laborea.</p>
<p class="step-p" style="left:616px">Lorem ipsum dolor sit amet, consectetur adipiscing elit, sed do eiusmod tempor incidi laborea.</p>
<p class="step-p" style="left:867px">Lorem ipsum dolor sit amet, consectetur adipiscing elit, sed do eiusmod tempor incidi laborea.</p>
<div class="btn navy" style="left:498px;top:2667px;width:204px;height:40px">Join a Free Session</div>

<!-- Articles -->
<h2 class="abs heading" style="left:0;top:2878px;width:1200px;font-size:48px">LATEST ARTICLES</h2>
<div class="underline" style="top:2937px"></div>

<div class="abs" role="img" aria-label="Photo of a counsellor talking with a client in a bright room" style="left:113px;top:2974px;width:446px;height:283px;border-radius:18px 18px 18px 0;background:linear-gradient(90deg,#cfd6dc,#e7e5e1 55%,#c7b3a5)"></div>
<div class="abs" style="left:158px;top:3208px;width:401px;height:175px;background:#f4f4f4;border-radius:18px;padding:40px 24px 0"></div>
<div class="abs date" style="left:183px;top:3192px">&#9638; 30 JAN 2026</div>
<div class="abs art-t" style="left:182px;top:3240px;width:360px">Lorem ipsum dolor sit amet consectetur adipiscing</div>
<p class="abs" style="left:182px;top:3294px;width:350px;font-size:14px;line-height:22px;color:#444">Sed ut perspiciatis unde omnis iste natus error sit voluptatem accusantium...</p>
<div class="abs more" style="left:182px;top:3346px">READ MORE</div>

<div class="abs" role="img" aria-label="Photo of a stressed woman holding her head at a laptop" style="left:573px;top:2974px;width:251px;height:196px;border-radius:18px;background:linear-gradient(135deg,#d9d4cd,#c86a5a 50%,#b9b4ad)"></div>
<div class="abs date" style="left:848px;top:2996px">&#9638; 30 JAN 2026</div>
<div class="abs art-t" style="left:848px;top:3044px;width:240px">Lorem ipsum dolor sit amet consectetur adipiscing</div>
<div class="abs more" style="left:848px;top:3133px">READ MORE</div>

<div class="abs" role="img" aria-label="Photo of a hiker climbing rocks against a bright sunset" style="left:573px;top:3188px;width:251px;height:195px;border-radius:18px;background:linear-gradient(135deg,#f0c77a,#a86a3a 50%,#3b2b22)"></div>
<div class="abs date" style="left:848px;top:3209px">&#9638; 30 JAN 2026</div>
<div class="abs art-t" style="left:848px;top:3257px;width:240px">Lorem ipsum dolor sit amet consectetur adipiscing</div>
<div class="abs more" style="left:848px;top:3346px">READ MORE</div>

<!-- Footer -->
<svg class="abs" style="left:0;top:3460px" width="1200" height="110" viewBox="0 0 1200 110">
  <path d="M0,110 C200,-20 420,10 640,50 C860,90 1040,80 1200,10 L1200,110 Z" fill="var(--navy)"/>
  <path d="M0,105 C180,-10 420,0 640,40 C860,80 1040,70 1200,0 L1200,18 C1040,90 860,100 640,62 C420,22 200,5 0,110 Z" fill="var(--green)"/>
</svg>
<div class="abs footer"></div>
<div class="abs" style="left:109px;top:3753px;font-family:'Lato',sans-serif;font-weight:700;font-size:31px;line-height:38px;color:var(--white)">QUIETFERN<br>MEDITATION</div>

<div class="abs f-h" style="left:347px;top:3676px">QUICK LINKS</div>
<ul class="abs links" style="left:347px;top:3710px">
  <li>Home</li><li>About the Organisation</li><li>Meditation Sessions</li><li>Events &amp; Programs</li><li>Resources</li><li>Contact Us</li>
</ul>

<div class="abs f-h" style="left:571px;top:3676px">CONTACT US</div>
<div class="ci" style="left:571px;top:3716px"><svg width="16" height="18" viewBox="0 0 16 18"><path d="M8,0 a7,7 0 0 1 7,7 c0,5 -7,11 -7,11 s-7,-6 -7,-11 a7,7 0 0 1 7,-7 Z" fill="var(--green)"/><circle cx="8" cy="7" r="2.5" fill="#fff"/></svg></div>
<div class="abs cl" style="left:629px;top:3718px;width:200px">LOCATIONS:<small>12 Willowbank Lane, Ferndale, Australia</small></div>
<div class="ci" style="left:571px;top:3786px"><svg width="16" height="16" viewBox="0 0 16 16"><path d="M3,1 L6,1 L7,5 L5,6.5 C6,9 7,10 9.5,11 L11,9 L15,10 L15,13 C15,14 14,15 13,15 C6,15 1,10 1,3 C1,2 2,1 3,1 Z" fill="var(--green)"/></svg></div>
<div class="abs cl" style="left:629px;top:3788px">PHONE:<small>+61 (02) 5550 1234</small></div>
<div class="ci" style="left:571px;top:3840px"><svg width="16" height="12" viewBox="0 0 16 12"><rect width="16" height="12" rx="1.5" fill="var(--green)"/><path d="M1,1 L8,7 L15,1" stroke="#fff" stroke-width="1.5" fill="none"/></svg></div>
<div class="abs cl" style="left:629px;top:3842px">EMAIL:<small>hello@quietfernmeditation.org</small></div>

<div class="btn" style="left:831px;top:3683px;width:257px;height:46px;font-weight:500;font-size:15px">Volunteer With Us</div>
<div class="btn" style="left:831px;top:3741px;width:257px;height:46px;background:var(--white);color:var(--navy);font-weight:500;font-size:15px">Donate Now</div>

<div class="abs" style="left:109px;top:3928px;width:979px;height:1px;background:rgba(255,255,255,.25)"></div>
<div class="abs" style="left:0;top:3950px;width:1200px;text-align:center;color:var(--white);font-size:11px">© 2026 QUIETFERN MEDITATION &nbsp;|&nbsp; Privacy Policy</div>
<div class="abs social" style="left:933px;top:3941px"><i style="border-color:#fff"></i><i class="on"></i><i style="border-color:#fff"></i><i style="border-color:#fff"></i></div>

</body>
</html>
```